*URGENT! FINE TIP INCLUDED* PARTY FLYER NEEDED FOR NYC HIP HOP EVENT ASAP!!!

Examples of NYC party flyers are in the attached files, please utilize the given professionally taken photos attached as well as anything else provided.

⚠️ADDITIONALLY⚠️
please make the flyer have a color coded rhyme scheme theme on paper/note book feel (if unsure what that is please refer to the mask with the notebook with colors on it, as well as other referenced images given in the attachment) no specific words need to be used but please have the color codes blurred in the background with complexed pattern of colors.

What we need to say on the flyer:
- (Title of event)
RoKai’s 20th Rapiversary Celebration
(RoKai should be exactly how it is spelled as read, the capital J and capital Z, the rest lower case)

- (Sub title / explanation of event)
Celebrating 20 Years Of A Rapping Lifestyle And Hobby With The REAL Hip Hop/Rap Music Eras & Artists ONLY!!!
70s 80s 90s 2000s Block Party (make sure this is able to be seen clearly as well as the main title)

VISION FOR THE FLYER (It will be both advertised through campaigning & printed out so please meet all expectations as soon as possible today or this weekend as time is very crucial) :

1. Integrate both a modern / old school feel with masculine fonts

2. The given professional photos of RoKai (see attached) posted around the flyer

3. PLEASE utilize RoKai’s official logo on the cover as well (provided in attachments)

INFORMATION OF THE EVENT (towards bottom half of flyer) :
- Address: Linwell Street Between Dorrance & Kemble Avenue
Brooklyn, NY 11583

- Transportation: East New York Bound B6 Bus to Tarrow Fields Avenue Or B14 to Dorrance Avenue & Halvern Street
GPS For Driving Use: 427 Dorrance Ave, Brooklyn, NY 11583
Trains: C train to Quinlan avenue
3 or 2 Train to Tarrow Fields Avenue

- Time: 12pm-9pm
- Date: September 18 2021

Please meet all detailed requests. We need this as fast, but efficient as possible. I will provide photos in both png and image as needed. I am not sure what is needed for the logo so png and image will be provided, just the face and name is needed not the (black or white) background. If there is anything else we can provide please contact.

⚠️LASTLY⚠️
*The leading image towards center should be the image provided with RoKai crossing arms with pencil and pen + to its side the image with RoKai holding the notebook showing the color highlighted rhyme schemes + all other given professional photos in the attachment scattered around the flyer as possible.

Please & Thank you.

Requirements
Must have
• ALL provided shots of RoKai around the flyer | Color highlighted rhyme scheme with notebook feel | The given title and subtitle explaining the event VIVIDLY & BOLD | Everything explained in the project brief *please read*
Should not have
• JUST 1 photo of RoKai.

```html
<!DOCTYPE html>
<html lang="en">
<head>
<meta charset="utf-8">
<title>RoKai’s 20th Rapiversary Celebration</title>
<link rel="stylesheet" href="https://fonts.googleapis.com/css2?family=Montserrat:wght@700;800&family=Bebas+Neue&family=Oswald:wght@700&display=swap">
<style>
  :root {
    --page: #ffffff;
    --ink: #111111;
    --red: #d9544a;
    --blue: #1a8fd0;
    --cyan: #4fc8ee;
    --green: #5fe85a;
    --yellow: #e5ee1c;
    --bright-red: #e8141a;
    --silver-1: #9c9c9c;
    --silver-2: #e6e6e6;
    --maroon: #3a0d0d;
    --footer: #050505;
    --time-blue: #1aa8e8;
  }
  * { box-sizing: border-box; margin: 0; padding: 0; }
  html, body { width: 1200px; height: 1200px; overflow: hidden; background: var(--page); }
  body { position: relative; font-family: "Montserrat", Arial, sans-serif; }

  .flyer {
    position: absolute; left: 203px; top: 84px; width: 801px; height: 1038px;
    overflow: hidden; box-shadow: 0 2px 8px rgba(0,0,0,.25);
  }
  .rhyme-backdrop {
    position: absolute; inset: 0;
    background:
      radial-gradient(circle at 15% 20%, rgba(230,40,130,.55), transparent 30%),
      radial-gradient(circle at 55% 8%, rgba(40,210,60,.6), transparent 28%),
      radial-gradient(circle at 90% 25%, rgba(220,40,160,.5), transparent 30%),
      radial-gradient(circle at 10% 55%, rgba(60,190,230,.55), transparent 30%),
      radial-gradient(circle at 90% 60%, rgba(50,200,80,.5), transparent 30%),
      radial-gradient(circle at 20% 80%, rgba(230,80,60,.5), transparent 28%),
      radial-gradient(circle at 85% 82%, rgba(60,180,230,.5), transparent 28%),
      linear-gradient(#e8e0e8, #e0eadc);
  }
  .photo { position: absolute; }
  .photo-left { left: 56px; top: 180px; width: 232px; height: 230px;
    background: linear-gradient(160deg, #2a2a2a, #7a4a3a 60%, #1a1a1a); border-radius: 90px 90px 0 0; }
  .photo-right { left: 570px; top: 162px; width: 148px; height: 248px;
    background: linear-gradient(160deg, #222, #7a4a3a 60%, #1a1a1a); border-radius: 70px 70px 0 0; }
  .photo-main { left: 282px; top: 35px; width: 310px; height: 375px;
    background: linear-gradient(170deg, #111 0%, #2a2a2a 40%, #8a5040 70%, #1b1b1b 100%); border-radius: 150px 150px 0 0; }
  .photo-inset { left: 544px; top: 607px; width: 200px; height: 135px;
    background: linear-gradient(90deg, #111 0%, #3a2a24 50%, #d8d8d8 70%, #f0f0f0 100%);
    border: 3px solid #bdbdbd; }

  .brand { position: absolute; left: 72px; top: 132px; display: flex; align-items: center; gap: 8px; }
  .brand-dot { width: 22px; height: 22px; border-radius: 50%; background: var(--bright-red); }
  .brand-name { font-weight: 800; font-size: 28px; color: var(--ink); }

  .title-plate {
    position: absolute; top: 410px; height: 118px;
    background: linear-gradient(110deg, var(--silver-1), var(--silver-2) 45%, var(--silver-1) 70%, var(--silver-2));
    border: 3px solid #d4d4d4; display: flex; align-items: center; justify-content: center;
  }
  .title-name { left: 64px; width: 505px; font-family: "Montserrat", sans-serif; font-weight: 800;
    font-size: 94px; color: var(--ink); letter-spacing: -1px; }
  .title-year { left: 581px; width: 163px; font-family: "Oswald", sans-serif; font-weight: 700;
    font-size: 92px; color: var(--maroon); }
  .title-year sup { font-family: "Montserrat", serif; font-size: 32px; font-weight: 700; vertical-align: 38px; }

  .band { position: absolute; top: 539px; height: 58px; color: #fff; font-weight: 700;
    font-size: 37px; display: flex; align-items: center; justify-content: center; letter-spacing: 1px; white-space: nowrap; }
  .band-red { left: 64px; width: 337px; background: var(--red); }
  .band-blue { left: 414px; width: 330px; background: var(--blue); }

  .tagline { position: absolute; left: 64px; top: 620px; width: 460px; font-weight: 700;
    font-size: 20px; line-height: 28px; color: var(--ink); }
  .tagline mark { color: var(--ink); padding: 0 4px; }
  .hl-red { background: var(--red); }
  .hl-yellow { background: var(--yellow); }
  .hl-cyan { background: var(--cyan); }

  .party { position: absolute; top: 754px; height: 62px; overflow: hidden; white-space: nowrap;
    display: flex; align-items: center; justify-content: center; }
  .party span { display: block; font-family: "Bebas Neue", sans-serif; font-size: 60px; line-height: 1;
    color: var(--ink); transform: scaleY(1.15); padding-top: 6px; }
  .party-eras { left: 64px; width: 399px; background: var(--green); }
  .party-block { left: 467px; width: 277px; background: var(--yellow); }

  .stripe { position: absolute; left: 0; top: 837px; width: 801px; height: 18px; display: flex; gap: 4px; background: var(--footer); }
  .stripe span { flex: 1; }

  .info { position: absolute; left: 0; top: 855px; width: 801px; height: 183px; background: var(--footer); }
  .info-line { position: absolute; font-weight: 700; white-space: nowrap; line-height: 1.3; }
  .info-line mark { color: var(--ink); padding: 0 5px; }
  .left-col { right: 480px; text-align: right; }
  .right-col { left: 417px; }
  .tag-yellow { background: var(--yellow); }
  .tag-red { background: var(--bright-red); color: #fff !important; }
  .sm { font-size: 14px; }
  .xs { font-size: 12px; }
  .time { font-size: 25px; color: var(--time-blue); }
  .date { font-size: 25px; }
  .icon { position: absolute; }
  .divider { position: absolute; left: 374px; top: 20px; width: 2px; height: 116px; background: #888; }
</style>
</head>
<body>
<div class="flyer">
  <div class="rhyme-backdrop" role="img" aria-label="Blurred colour-coded rhyme scheme highlights on notebook paper"></div>

  <div class="brand"><span class="brand-dot"></span><span class="brand-name">RoKai</span></div>

  <div class="photo photo-left" role="img" aria-label="Photo of RoKai in a hood writing in a notebook"></div>
  <div class="photo photo-right" role="img" aria-label="Photo of RoKai crouching with a colour-highlighted notebook"></div>
  <div class="photo photo-main" role="img" aria-label="Photo of RoKai in a hood with crossed arms holding a pencil and pen"></div>

  <div class="title-plate title-name">RoKai’s</div>
  <div class="title-plate title-year">20<sup>th</sup></div>

  <div class="band band-red">RAPIVERSARY</div>
  <div class="band band-blue">CELEBRATION</div>

  <p class="tagline">Celebrating <mark class="hl-red">20 Years</mark> Of <mark class="hl-yellow">A Rapping</mark> <mark class="hl-cyan">Lifestyle</mark> And <mark class="hl-yellow">Hobby</mark> With <mark class="hl-cyan">The REAL</mark> <mark class="hl-cyan">Hip Hop/Rap</mark> <mark class="hl-red">Music Eras &amp; Artists</mark> <mark class="hl-red">ONLY!!!</mark></p>

  <div class="photo photo-inset" role="img" aria-label="Photo of RoKai holding a pencil beside a colour-coded rhyme notebook"></div>

  <div class="party party-eras"><span>70S 80S 90S 2000S</span></div>
  <div class="party party-block"><span>BLOCK PARTY</span></div>

  <div class="stripe">
    <span style="background:#c44a32"></span><span style="background:#b0387a"></span><span style="background:#bfc81e"></span><span style="background:#e8141a"></span><span style="background:#1a8fd0"></span><span style="background:#d8d8d8"></span><span style="background:#2fb03a"></span><span style="background:#9a2fb0"></span><span style="background:#c0a8dc"></span><span style="background:#ee5a30"></span><span style="background:#1a8fd0"></span><span style="background:#eef01a"></span><span style="background:#e8141a"></span><span style="background:#e8141a"></span>
  </div>

  <div class="info">
    <div class="info-line left-col sm" style="top:19px"><mark class="tag-yellow">C train to Quinlan avenue</mark></div>
    <div class="info-line left-col sm" style="top:38px"><mark class="tag-yellow">3 or 2 Train to Tarrow Fields Avenue</mark></div>
    <div class="info-line left-col time" style="top:66px">12pm-9pm</div>
    <div class="info-line left-col date" style="top:109px"><mark class="tag-red">September 18,</mark><mark class="tag-yellow">2021</mark></div>

    <svg class="icon" style="left:334px;top:21px" width="22" height="26" viewBox="0 0 22 26" fill="none" stroke="#fff" stroke-width="2"><rect x="3" y="2" width="16" height="16" rx="4"/><line x1="3" y1="10" x2="19" y2="10"/><circle cx="7.5" cy="14" r="1" fill="#fff"/><circle cx="14.5" cy="14" r="1" fill="#fff"/><line x1="6" y1="18" x2="3" y2="24"/><line x1="16" y1="18" x2="19" y2="24"/></svg>
    <svg class="icon" style="left:334px;top:72px" width="22" height="22" viewBox="0 0 22 22" fill="none" stroke="#fff" stroke-width="2"><circle cx="11" cy="11" r="9"/><polyline points="11,5 11,11 15,13"/></svg>
    <svg class="icon" style="left:334px;top:115px" width="22" height="22" viewBox="0 0 22 22" fill="none" stroke="#fff" stroke-width="2"><rect x="2" y="4" width="18" height="16" rx="2"/><line x1="2" y1="9" x2="20" y2="9"/><line x1="7" y1="1" x2="7" y2="6"/><line x1="15" y1="1" x2="15" y2="6"/></svg>

    <div class="divider"></div>

    <svg class="icon" style="left:390px;top:17px" width="18" height="24" viewBox="0 0 18 24"><path d="M9 0C4 0 0 4 0 9c0 7 9 15 9 15s9-8 9-15c0-5-4-9-9-9z" fill="#fff"/><circle cx="9" cy="9" r="3.5" fill="#050505"/></svg>
    <svg class="icon" style="left:389px;top:68px" width="20" height="22" viewBox="0 0 20 22" fill="none" stroke="#fff" stroke-width="2"><rect x="2" y="2" width="16" height="15" rx="3"/><line x1="2" y1="10" x2="18" y2="10"/><line x1="5" y1="17" x2="5" y2="21"/><line x1="15" y1="17" x2="15" y2="21"/></svg>

    <div class="info-line right-col xs" style="top:19px"><mark class="tag-yellow">Linwell Street Between Dorrance &amp; Kemble Avenue</mark></div>
    <div class="info-line right-col xs" style="top:37px"><mark class="tag-yellow">Brooklyn, NY 11583</mark></div>
    <div class="info-line right-col xs" style="top:68px"><mark class="tag-yellow">East New York Bound B6 Bus to Tarrow Fields Avenue</mark></div>
    <div class="info-line right-col xs" style="top:86px"><mark class="tag-yellow">Or B14 to Dorrance Avenue &amp; Halvern Street</mark></div>
    <div class="info-line right-col xs" style="top:116px"><mark class="tag-red">GPS For Driving Use:</mark><mark class="tag-yellow">427 Dorrance Ave, Brooklyn,</mark></div>
    <div class="info-line right-col xs" style="top:134px"><mark class="tag-yellow">NY 11583</mark></div>
  </div>
</div>
</body>
</html>
```